【重要事項】
ワードプレスでのホームページ制作依頼、別途予定あり
デザインから制作まで一貫して行える方はご相談ください。
トップページデザインのみのご提案ももちろん大歓迎です。

【トップページデザインの要望】
・コンパクトでユーザーフレンドリー、お客様を意識したトップページ
サイトを訪れた人が求める情報にすぐアクセスできるデザインを希望します。詳細は添付ファイルをご覧ください。

【弊社ホームページ】
リニューアル対象のホームページURLのほか下記
http://rokugaen-shop.jp/
園芸のECサイトです。

【添付ファイル】
共有事項は添付ファイルにまとめています。お手数ですがご一読ください。
ロゴもございます。デザイン作成にお役立てください。
http://rokugaen.jp/
1ページ
緑系
• 高解像度JPG (.jpg)
• PNG形式 (.png)
8/31追記(質問への回答まとめ)

【納品形式の追加】
ai形式/PSD形式の納品可
※要望には個別でも柔軟に対応します。

【ロゴデータの追加】
pngデータ2つ、jpgデータ1つ
色のこだわりは強くありません。デザインに合わせてご活用ください。

【参考にしたいサイト】
https://q-m.co.jp/
最近できた会社様で、お客様目線に振り切ったデザインです。
ここまでポップにはできませんが、取り入れられる要素は取り入れたいと思っています。

https://www.nuvo-greno.com/
競合他社様ですが、多言語対応できるデザインレイアウトが印象的です。
弊社も英語対応のホームページ(弊社にて文言を翻訳)にする予定です。

みなさまのご応募お待ちしております。

当選者:桐山様
当選理由:社内会議による選考の末、多数決により決定しました。
色合いとデザインの段組が非常に優れておりました。
次点入選:blinker様、ree様
入選理由:blnker様は社内会議で最後まで当選作品と一、二を争う優秀作品でした。
特にイラストのテイストが社長の好みに合っており好印象でした。
ree様は写真の選定センス、全体のデザイン感が女性社員に受けました。

今回は担当が変わってから初めての提案でした。
不慣れなことが多い中、たくさんのご提案をいただき、様々な改善点や面白いデザイン、よりよいHPづくりのヒントをランサーのエキスパートの皆様よりいただきました。
誠にお礼申し上げます。

また、後半ご提出のご提案には、逐一ご挨拶ができず申し訳ございませんでした。
今回いただけた縁を活かして、よりよいHP制作につなげていきたいと考えております。

惜しくも当選、入選とならなかった皆様にも、心よりお礼を申し上げます。
またの機会がございましたら、よろしくお願いします。

```html
<!DOCTYPE html>
<html lang="ja">
<head>
<meta charset="utf-8">
<title>六雅園 トップページ</title>
<link href="https://fonts.googleapis.com/css2?family=Noto+Sans+JP:wght@400;500;700&family=Noto+Serif+JP:wght@500;700&family=Oswald:wght@300;400;500&display=swap" rel="stylesheet">
<style>
:root{
  --green:#2f7d3b;
  --green-dark:#1e5f2a;
  --green-soft:#e9f1ec;
  --brown:#a8643a;
  --blue-soft:#eaf1f8;
  --ink:#333;
  --muted:#888;
  --line:#d6d6d6;
  --white:#fff;
}
*{box-sizing:border-box;margin:0;padding:0}
html,body{width:1200px;height:3060px;overflow:hidden}
body{position:relative;background:var(--white);color:var(--ink);font-family:"Noto Sans JP",sans-serif}
.abs{position:absolute}
.en{font-family:"Oswald",sans-serif;font-weight:300;letter-spacing:.06em}
.serif{font-family:"Noto Serif JP",serif}
.photo{position:absolute}

/* header */
.brand{left:60px;top:38px;color:var(--green);font-family:"Oswald",sans-serif;font-weight:500;font-size:40px;letter-spacing:.02em}
.brand-sub{left:62px;top:88px;font-size:11px;color:var(--green);letter-spacing:.2em}
.nav{left:780px;top:48px;display:flex;gap:22px;font-size:13px;color:var(--ink)}
.contact-tab{right:0;top:0;width:72px;height:150px;background:var(--green);color:#fff;font-size:12px;display:flex;flex-direction:column;align-items:center;justify-content:center;gap:10px}
.contact-tab svg{width:22px;height:22px}

/* hero */
.hero-photo{left:220px;top:30px;width:980px;height:610px;background:linear-gradient(180deg,#cfe9f5 0%,#9bd37a 22%,#5fae3e 60%,#3f8f2b 100%)}
.hero-copy{left:72px;top:270px;font-size:38px;font-weight:700;line-height:1.45;letter-spacing:.04em}
.hero-lead{left:72px;top:392px;width:360px;font-size:12px;line-height:1.8;color:var(--ink)}
.hero-card{top:228px;width:176px;height:186px;color:#fff;padding:20px 14px;text-align:center}
.hero-card .ico{width:96px;height:64px;margin:6px auto 14px;background:rgba(255,255,255,.25);border-radius:4px}
.hero-card p{font-size:15px;font-weight:700;line-height:1.5}
.card-animal{left:492px;background:var(--green)}
.card-plant{left:680px;background:var(--brown)}
.scroll-line{left:60px;top:470px;width:1px;height:150px;background:var(--ink)}
.scroll-text{left:44px;top:440px;font-size:11px;transform:rotate(90deg);transform-origin:left top}

/* about */
.about-band{left:0;top:690px;width:1200px;height:470px;background:var(--blue-soft)}
.about-photo{left:0;top:680px;width:600px;height:520px;background:linear-gradient(160deg,#cfe0ee 0%,#9fb4c4 45%,#4c4c4c 100%)}
.sec-title{font-size:40px;color:var(--green)}
.sec-sub{font-size:12px;color:var(--muted)}
.about-title{left:660px;top:740px}
.about-sub{left:662px;top:792px}
.about-head{left:660px;top:830px;font-size:26px;line-height:1.55;color:var(--ink)}
.about-text{left:660px;top:930px;width:430px;font-size:12px;line-height:1.9;color:var(--ink)}
.btn{display:flex;align-items:center;justify-content:center;gap:14px;height:40px;width:160px;border:1px solid var(--green);color:var(--green);font-size:12px;background:#fff;letter-spacing:.1em}
.btn::after{content:"";width:30px;height:1px;background:currentColor}
.about-btn{left:660px;top:1050px}

/* business / office */
.tile{top:1160px;width:346px;height:260px;color:#fff;padding:26px 28px}
.tile-business{left:228px;background:linear-gradient(135deg,#7a5a42,#3b2e24)}
.tile-office{left:628px;background:linear-gradient(135deg,#3f5a7a,#1f2a36)}
.tile-title{font-size:34px}
.tile-sub{font-size:12px;margin-top:-2px}
.tile-text{font-size:11px;line-height:1.8;margin-top:12px;text-align:center}
.tile .btn{position:absolute;left:93px;bottom:26px;border-color:#fff;color:#fff;background:transparent}

/* shop banner */
.shop{left:228px;top:1492px;width:746px;height:226px;background:linear-gradient(90deg,#6c8c5e,#c7b79a 45%,#7d9a6a 100%)}
.shop-badge{left:530px;top:1530px;width:140px;height:150px;background:#fff;border:2px solid var(--green);display:flex;flex-direction:column;align-items:center;justify-content:center;gap:8px}
.shop-badge .dot{width:44px;height:44px;border-radius:50%;background:var(--green)}
.shop-badge .name{font-family:"Noto Serif JP",serif;font-size:22px;font-weight:700;color:var(--green)}
.shop-badge .en-s{font-size:12px;color:var(--green);letter-spacing:.15em}

/* recruit */
.recruit{left:64px;top:1750px;width:540px;height:272px;background:var(--green);color:#fff}
.recruit-title{left:100px;top:1778px;font-size:34px;color:#fff}
.recruit-sub{left:102px;top:1824px;font-size:12px;color:#fff}
.recruit-head{left:290px;top:1770px;font-size:32px;font-weight:700;color:#fff}
.recruit-text{left:290px;top:1830px;width:280px;font-size:12px;line-height:1.9;color:#fff}
.recruit-btn{left:290px;top:1950px;width:150px;border-color:#fff;color:#fff;background:transparent}
.recruit-grid{left:600px;top:1750px;width:600px;height:272px;display:grid;grid-template-columns:repeat(4,1fr);grid-template-rows:1fr 1fr;gap:2px}
.recruit-grid div{background:linear-gradient(160deg,#5d6f86,#2c3442)}
.recruit-grid div:nth-child(odd){background:linear-gradient(160deg,#8a9bb0,#3b4656)}

/* news */
.news-title{left:228px;top:2104px}
.news-sub{left:230px;top:2155px}
.news-btn{left:228px;top:2198px;width:110px}
.news-list{left:420px;top:2100px;width:560px;list-style:none}
.news-list li{display:flex;gap:28px;padding:18px 0;border-bottom:1px solid var(--line);font-size:12px}
.news-list time{color:var(--green);font-family:"Oswald",sans-serif}

/* photolog */
.gallery-bg{left:0;top:2320px;width:1200px;height:440px;background:var(--green-soft)}
.gallery-title{left:0;top:2366px;width:1200px;text-align:center}
.gallery-sub{left:0;top:2418px;width:1200px;text-align:center}
.gallery-row{left:60px;top:2452px;width:1080px;height:206px;display:grid;grid-template-columns:repeat(5,1fr);gap:10px}
.gallery-row div{background:linear-gradient(160deg,#8aa07a,#4b5a3c)}
.gallery-row div:nth-child(2n){background:linear-gradient(160deg,#a7927a,#5a4a3a)}
.arrow{top:2540px;width:34px;height:34px;border-radius:50%;background:var(--green);display:flex;align-items:center;justify-content:center}
.arrow svg{width:14px;height:14px}
.gallery-btn{left:525px;top:2692px;width:150px}

/* footer */
.f-brand{left:228px;top:2850px;font-family:"Oswald",sans-serif;font-weight:500;font-size:38px;color:var(--green)}
.f-company{left:230px;top:2902px;font-size:12px}
.f-tel{left:230px;top:2922px;font-size:22px;font-weight:700;color:var(--green);font-family:"Oswald",sans-serif}
.f-info{left:230px;top:2958px;font-size:11px;line-height:1.7;color:var(--muted)}
.f-nav{top:2854px;list-style:none;font-size:11px;line-height:2.2}
.f-nav1{left:668px}.f-nav2{left:800px}
.f-social{left:900px;top:2860px;display:flex;gap:8px}
.f-social span{width:18px;height:18px;border-radius:50%;background:var(--ink)}
.copyright{left:0;top:3030px;width:1200px;text-align:center;font-size:10px;color:var(--muted)}
.pagetop{right:14px;top:2720px;width:40px;height:40px;background:var(--green);display:flex;align-items:center;justify-content:center}
</style>
</head>
<body>

<header>
  <div class="abs brand">Rokugaen</div>
  <div class="abs brand-sub">株式会社六雅園</div>
  <nav class="abs nav"><span>会社概要</span><span>事業内容</span><span>拠点紹介</span><span>採用情報</span><span>お知らせ</span></nav>
  <a class="abs contact-tab">
    <svg viewBox="0 0 24 24" fill="none" stroke="#fff" stroke-width="1.6"><rect x="3" y="5" width="18" height="14"/><path d="M3 6l9 7 9-7"/></svg>
    <span>お問い合わせ</span>
  </a>
</header>

<section class="hero">
  <div class="photo hero-photo" role="img" aria-label="青空の下、緑の牧草地で草を食む乳牛たち"></div>
  <h1 class="abs hero-copy">動物や植物を通して<br>豊かな生活を。</h1>
  <p class="abs hero-lead">株式会社六雅園は動物医薬品や農業資材を幅広く取り扱い、地域の暮らしを支えています。</p>
  <a class="abs hero-card card-animal"><div class="ico" role="img" aria-label="牛・豚・鶏・犬猫のイラスト"></div><p>牛・豚・鶏・犬猫の<br>お客様はこちらへ!</p></a>
  <a class="abs hero-card card-plant"><div class="ico" role="img" aria-label="トラクターと植物のイラスト"></div><p>農業・園芸の<br>お客様はこちらへ!</p></a>
  <div class="abs scroll-line"></div>
</section>

<section class="about">
  <div class="abs about-band"></div>
  <div class="photo about-photo" role="img" aria-label="こちらを見つめる白黒の乳牛たち"></div>
  <h2 class="abs en sec-title about-title">ABOUT US</h2>
  <p class="abs sec-sub about-sub">会社案内</p>
  <p class="abs serif about-head">動物医薬品や農業資材を<br>幅広く取り扱っております</p>
  <p class="abs about-text">当社は創業以来、畜産農家と園芸農家の皆様に寄り添い、動物医薬品や農業資材を届けてまいりました。確かな品質と丁寧な対応で、地域の生産者の毎日を支え続けます。</p>
  <a class="abs btn about-btn">MORE</a>
</section>

<section>
  <a class="abs tile tile-business" role="img" aria-label="手に取った苗と作業風景">
    <div class="en tile-title">BUSINESS</div><div class="tile-sub">事業内容</div>
    <p class="tile-text">動物医薬品事業・農業資材事業<br>園芸事業を展開しています</p>
    <span class="btn">MORE</span>
  </a>
  <a class="abs tile tile-office" role="img" aria-label="営業所の外観">
    <div class="en tile-title">OFFICE</div><div class="tile-sub">拠点紹介</div>
    <p class="tile-text">本社・営業所の所在地と<br>各拠点の紹介はこちら</p>
    <span class="btn">MORE</span>
  </a>
</section>

<section>
  <div class="photo shop" role="img" aria-label="店頭に並ぶ鉢植えと園芸用品"></div>
  <a class="abs shop-badge"><span class="dot"></span><span class="name">六雅園</span><span class="en en-s">ONLINE SHOP</span></a>
</section>

<section>
  <div class="abs recruit"></div>
  <h2 class="abs en recruit-title">RECRUIT</h2>
  <p class="abs recruit-sub">採用情報</p>
  <p class="abs serif recruit-head">先輩に続け!</p>
  <p class="abs recruit-text">地域の農業と畜産を支える仲間を募集しています。先輩社員の声や働く環境をご紹介します。</p>
  <a class="abs btn recruit-btn">採用情報</a>
  <div class="abs recruit-grid" role="img" aria-label="働く社員たちの写真">
    <div></div><div></div><div></div><div></div><div></div><div></div><div></div><div></div>
  </div>
</section>

<section>
  <h2 class="abs en sec-title news-title">NEWS</h2>
  <p class="abs sec-sub news-sub">お知らせ</p>
  <a class="abs btn news-btn">VIEW ALL</a>
  <ul class="abs news-list">
    <li><time>2021.09.01</time><span>ホームページをリニューアルしました。</span></li>
    <li><time>2021.08.20</time><span>夏季休業期間のお知らせ</span></li>
    <li><time>2021.08.02</time><span>新商品の取り扱いを開始しました。</span></li>
  </ul>
</section>

<section>
  <div class="abs gallery-bg"></div>
  <h2 class="abs en sec-title gallery-title">PHOTOLOG</h2>
  <p class="abs sec-sub gallery-sub">フォトギャラリー</p>
  <div class="abs gallery-row" role="img" aria-label="店頭の植物や商品の写真">
    <div></div><div></div><div></div><div></div><div></div>
  </div>
  <span class="abs arrow" style="left:26px"><svg viewBox="0 0 14 14" fill="none" stroke="#fff" stroke-width="2"><path d="M9 2L4 7l5 5"/></svg></span>
  <span class="abs arrow" style="left:1140px"><svg viewBox="0 0 14 14" fill="none" stroke="#fff" stroke-width="2"><path d="M5 2l5 5-5 5"/></svg></span>
  <a class="abs btn gallery-btn">FOLLOW US</a>
</section>

<footer>
  <div class="abs f-brand">Rokugaen</div>
  <p class="abs f-company">株式会社六雅園</p>
  <p class="abs f-tel">TEL 0000-12-3456</p>
  <p class="abs f-info">FAX 0000-12-3457<br>〒000-0000 緑野県青葉市若葉町1-2-3</p>
  <ul class="abs f-nav f-nav1"><li>HOME</li><li>会社概要</li><li>事業内容</li><li>拠点紹介</li><li>お知らせ</li></ul>
  <ul class="abs f-nav f-nav2"><li>採用情報</li><li>お問い合わせ</li><li>プライバシーポリシー</li></ul>
  <div class="abs f-social"><span></span><span></span><span></span></div>
  <a class="abs pagetop"><svg width="14" height="14" viewBox="0 0 14 14" fill="none" stroke="#fff" stroke-width="2"><path d="M2 9l5-5 5 5"/></svg></a>
  <p class="abs copyright">© ROKUGAEN Co., Ltd.</p>
</footer>

</body>
</html>
```